Bold Modern Creative Wine Label Needed for a Chardonnay

We need a modern, eye catching label, one that will appeal to millennials, but also attract the older more conservative crowd. We like the boldness of black on white but are open to your suggestions. Since the bottle type is a light green 'burgundy style' bottle, you should take that into account. The name of the brand is Vo`. The attached label is example of what we like very much. It is eye catching and bold and modern. Keep in mind that the bottle will be light green in color so black and white might not work so well. Use your creativity please! The label can be any size but needs to fit on this shape bottle. See attached photos. thanks!!

(Please no grapes or wine glasses or wine bottles featured on the label!)
Updates

Hi Designers, I just wanted to let you know that we received many great designs and we are sorting through them this week. The website is making it a bit difficult to create a 'poll' so this is taking longer than we expected. Thanks for all the great submissions!

```html
<!DOCTYPE html>
<html lang="en">
<head>
<meta charset="utf-8">
<title>Vò Chardonnay 2013 — Label Presentation</title>
<link href="https://fonts.googleapis.com/css2?family=Cormorant+Garamond:wght@500&family=Jost:wght@400&display=swap" rel="stylesheet">
<style>
  :root {
    --paper: #ffffff;
    --ink: #111111;
    --label-shadow: rgba(0, 0, 0, 0.32);
    --band-start: #231f20;
    --band-end: #444347;
    --band-ink: #ffffff;
    --band-rule: #d9d9d9;
    --glass-light: #d8cf72;
    --glass-dark: #5e5a1e;
  }
  html, body {
    margin: 0;
    padding: 0;
    width: 1200px;
    height: 999px;
    overflow: hidden;
    background: var(--paper);
  }
  .board {
    position: relative;
    width: 1200px;
    height: 999px;
    background: var(--paper);
  }
  .label {
    position: absolute;
    left: 145px;
    top: 133px;
    width: 645px;
    height: 557px;
    background: var(--paper);
    box-shadow: 0 0 60px 18px var(--label-shadow);
  }
  .label__name {
    position: absolute;
    left: 198px;
    top: 118px;
    margin: 0;
    font-family: "Cormorant Garamond", serif;
    font-weight: 500;
    font-size: 232px;
    line-height: 1;
    color: var(--ink);
  }
  .label__varietal {
    position: absolute;
    left: 200px;
    top: 358px;
    font-family: "Jost", sans-serif;
    font-size: 22px;
    color: var(--ink);
  }
  .label__vintage {
    position: absolute;
    left: 352px;
    top: 352px;
    font-family: "Jost", sans-serif;
    font-size: 31px;
    letter-spacing: 3px;
    color: var(--ink);
  }
  .label__rule {
    position: absolute;
    left: 458px;
    top: 372px;
    width: 187px;
    height: 2px;
    background: var(--ink);
  }
  .bottle {
    position: absolute;
    left: 935px;
    top: 205px;
    width: 128px;
    height: 540px;
    border-radius: 40px 40px 14px 14px;
    background: linear-gradient(90deg, var(--glass-dark), var(--glass-light) 55%, var(--glass-dark));
  }
  .band {
    position: absolute;
    left: 0;
    top: 800px;
    width: 1200px;
    height: 199px;
    background: linear-gradient(90deg, var(--band-start), var(--band-end));
  }
  .band__name {
    position: absolute;
    left: 74px;
    top: 52px;
    margin: 0;
    font-family: "Cormorant Garamond", serif;
    font-weight: 500;
    font-size: 84px;
    line-height: 1;
    color: var(--band-ink);
  }
  .band__rule {
    position: absolute;
    left: 178px;
    top: 103px;
    width: 1022px;
    height: 1px;
    background: var(--band-rule);
  }
</style>
</head>
<body>
  <main class="board">
    <section class="label" aria-label="Front label">
      <h1 class="label__name">Vò</h1>
      <span class="label__varietal">Chardonnay</span>
      <span class="label__vintage">2013</span>
      <span class="label__rule"></span>
    </section>

    <div class="bottle" role="img" aria-label="Light green burgundy-style bottle wearing the Vò label"></div>

    <footer class="band">
      <p class="band__name">Vò</p>
      <span class="band__rule"></span>
    </footer>
  </main>
</body>
</html>
```